Bref créative
Velvet Rooms
Home Interiors
Modern
Linnea Parcot Weller
Design Consultant
412 Quillon Lane
Ashmere Bay Gardens, QL 33587
LinneaParcot@velmorra.example
VelvetRooms.example
My logo is the Velvet Rooms. Would like to incorporate a flur de lis.

```html
<!DOCTYPE html>
<html lang="en">
<head>
<meta charset="utf-8">
<title>Velvet Rooms – Business Card</title>
<link href="https://fonts.googleapis.com/css2?family=Merriweather:wght@400;700&display=swap" rel="stylesheet">
<style>
  :root {
    --backdrop: #e6e3df;
    --card-white: #ffffff;
    --brand-red: #c8202e;
    --brand-red-light: #dc3440;
    --brand-red-dark: #a8141f;
    --ink-black: #111111;
    --logo-grey: #3a3a3a;
    --text-white: #ffffff;
  }
  * { margin: 0; padding: 0; box-sizing: border-box; }
  html, body {
    width: 1200px; height: 780px; overflow: hidden;
    background: var(--backdrop);
    font-family: "Merriweather", Georgia, serif;
  }
  .canvas { position: relative; width: 1200px; height: 780px; }
  .business-card {
    position: absolute; left: 80px; top: 90px;
    width: 1040px; height: 600px;
    border-radius: 36px; overflow: hidden;
    background: var(--card-white);
    box-shadow: 0 10px 30px rgba(0,0,0,0.18);
  }
  .card-waves { position: absolute; inset: 0; width: 100%; height: 100%; }
  .brand-mark {
    position: absolute; left: 330px; top: 130px;
    display: flex; align-items: center; gap: 22px;
  }
  .brand-dot { width: 34px; height: 34px; border-radius: 50%; background: var(--brand-red); }
  .brand-name {
    font-size: 44px; font-weight: 400; color: var(--logo-grey);
    letter-spacing: 1px; line-height: 1.1;
  }
  .person {
    position: absolute; right: 560px; top: 425px;
    text-align: right; color: var(--text-white);
  }
  .person-name { font-size: 29px; font-weight: 700; margin-bottom: 8px; }
  .person-title { font-size: 22px; margin-bottom: 18px; }
  .person-address { font-size: 21px; line-height: 1.45; }
  .divider {
    position: absolute; left: 510px; top: 395px;
    width: 2px; height: 170px; background: var(--text-white);
  }
  .contacts {
    position: absolute; left: 540px; top: 392px;
    list-style: none; color: var(--text-white); font-size: 20px;
  }
  .contacts li { display: flex; align-items: center; gap: 12px; height: 43px; }
  .contacts svg { width: 22px; height: 22px; flex: none; }
</style>
</head>
<body>
<div class="canvas">
  <article class="business-card">
    <svg class="card-waves" viewBox="0 0 1040 600" preserveAspectRatio="none" aria-hidden="true">
      <defs>
        <linearGradient id="redBand" x1="0" y1="0" x2="0" y2="1">
          <stop offset="0" stop-color="var(--brand-red-light)"/>
          <stop offset="0.6" stop-color="var(--brand-red)"/>
          <stop offset="1" stop-color="var(--brand-red-dark)"/>
        </linearGradient>
      </defs>
      <path d="M0,338 C260,395 620,385 1040,238 L1040,262 C620,410 260,420 0,362 Z" fill="var(--ink-black)"/>
      <path d="M0,370 C260,430 620,420 1040,272 L1040,600 L0,600 Z" fill="url(#redBand)"/>
    </svg>

    <div class="brand-mark">
      <span class="brand-dot"></span>
      <span class="brand-name">Velvet Rooms, LLC</span>
    </div>

    <div class="person">
      <p class="person-name">Linnea Parcot Weller</p>
      <p class="person-title">Design Consultant</p>
      <p class="person-address">412 Quillon Lane<br>Ashmere Bay Gardens, QL 33587</p>
    </div>

    <div class="divider"></div>

    <ul class="contacts">
      <li>
        <svg viewBox="0 0 24 24"><rect x="7" y="2" width="10" height="20" rx="2" fill="none" stroke="#fff" stroke-width="2"/><circle cx="12" cy="18" r="1.3" fill="#fff"/></svg>
        555.014.2207
      </li>
      <li>
        <svg viewBox="0 0 24 24"><path d="M3 9 C3 5 21 5 21 9 L18 11 L15 9 L9 9 L6 11 Z" fill="#fff"/><rect x="5" y="12" width="14" height="9" rx="1.5" fill="#fff"/></svg>
        555.018.3391
      </li>
      <li>
        <svg viewBox="0 0 24 24"><circle cx="12" cy="12" r="4" fill="none" stroke="#fff" stroke-width="2"/><path d="M16 8 V14 C16 17 21 17 21 12 A9 9 0 1 0 17 19.5" fill="none" stroke="#fff" stroke-width="2"/></svg>
        LinneaParcot@velmorra.example
      </li>
      <li>
        <svg viewBox="0 0 24 24"><circle cx="12" cy="12" r="9" fill="none" stroke="#fff" stroke-width="2"/><ellipse cx="12" cy="12" rx="4" ry="9" fill="none" stroke="#fff" stroke-width="1.6"/><path d="M3 12 H21" stroke="#fff" stroke-width="1.6"/></svg>
        VelvetRooms.example
      </li>
    </ul>
  </article>
</div>
</body>
</html>
```